Tail Meadow Website Design

Need a website for a Dog Grooiming business. Please make it simular to these:

https://www.wagtrolley.com
https://plainhaulo.com
https://thenookforkin.com
https://www.velmoro.com/portal/

```html
<!DOCTYPE html>
<html lang="en">
<head>
<meta charset="utf-8">
<title>Tail Meadow – Doorstep Dog Grooming</title>
<link rel="stylesheet" href="https://fonts.googleapis.com/css2?family=Roboto+Condensed:wght@700&family=Roboto:wght@400;500;700&display=swap">
<style>
:root{
  --green:#3db42f;
  --green-dark:#2f9a24;
  --blue:#1a7fd6;
  --blue-dark:#0f63b3;
  --ink:#222;
  --muted:#666;
  --white:#fff;
  --line:#dfe3e8;
}
*{box-sizing:border-box;margin:0;padding:0}
html,body{width:1200px;height:4180px;overflow:hidden}
body{position:relative;font-family:"Roboto",Arial,sans-serif;color:var(--ink);background:var(--white)}
.abs{position:absolute}
.head-font{font-family:"Roboto Condensed","Arial Narrow",sans-serif;font-weight:700;text-transform:uppercase}
.btn{display:inline-flex;align-items:center;justify-content:center;border-radius:30px;font-weight:700;font-size:14px;color:var(--white);letter-spacing:.5px;text-transform:uppercase}
.btn-green{background:var(--green)}

/* hero */
.hero{left:0;top:0;width:1200px;height:660px;background:linear-gradient(100deg,#0d5fb0 0%,#1f86dc 45%,#6fb6ea 75%,#2a7cc8 100%)}
.hero-shade{left:0;top:0;width:1200px;height:660px;background:linear-gradient(90deg,rgba(10,60,120,.55),rgba(10,60,120,0) 60%)}
.brand{left:112px;top:22px;color:var(--white);font-size:30px}
.nav{left:330px;top:30px;display:flex;gap:34px;font-size:14px;font-weight:700;color:var(--white)}
.nav .active{border-bottom:2px solid var(--white);padding-bottom:6px}
.call{left:836px;top:20px;width:254px;height:42px;font-size:13px}
.hero-title{left:112px;top:240px;color:var(--white);font-size:64px;line-height:66px}
.hero-text{left:112px;top:378px;width:430px;color:var(--white);font-size:15px;line-height:21px}
.book{left:112px;top:450px;width:160px;height:44px}
.form{left:632px;top:150px;width:456px;height:460px;background:var(--green);border-radius:22px;padding:22px 28px}
.form h2{color:var(--white);font-size:30px;margin-bottom:18px}
.field{background:var(--white);height:46px;border-radius:3px;font-size:14px;color:#888;padding:0 16px;display:flex;align-items:center;margin-bottom:18px}
.row{display:flex;gap:16px}.row .field{flex:1}
.select{justify-content:space-between}
.submit{background:var(--blue);height:48px;border-radius:3px;color:var(--white);font-weight:700;font-size:15px;display:flex;align-items:center;justify-content:center}

/* why */
.why-photo{left:168px;top:820px;width:410px;height:500px;border-radius:40% 40% 20% 20%;background:radial-gradient(ellipse at 50% 40%,#d9a35a,#b57a35 60%,#f3ece2 90%)}
.why-title{left:520px;top:824px;width:520px;text-align:center;font-size:40px}
.perks{left:490px;top:890px;width:580px;display:grid;grid-template-columns:repeat(3,1fr);row-gap:26px}
.perk{text-align:center;font-weight:700;font-size:18px;line-height:22px}
.perk svg{display:block;margin:0 auto 12px}

/* video */
.video{left:0;top:1440px;width:1200px;height:460px;background:linear-gradient(90deg,#d8cfc6 0%,#8a6a55 35%,#c48a55 60%,#e8dcd0 100%)}
.play{left:556px;top:1626px}

/* about */
.about-title{left:112px;top:1990px;font-size:40px}
.about-title span{color:var(--green)}
.about-text{left:112px;top:2050px;width:520px;font-size:15px;line-height:22px;color:var(--muted)}
.about-text p+p{margin-top:18px}
.learn{left:112px;top:2340px;width:170px;height:44px}
.about-photo{left:668px;top:1984px;width:420px;height:420px;border-radius:50%;background:radial-gradient(circle at 45% 40%,#f1d3bb,#c99a78 45%,#e8e4e0 80%)}

/* testimonials */
.reviews{left:0;top:2492px;width:1200px;height:580px;background:linear-gradient(135deg,#42b833,#2e9c23)}
.reviews-title{left:0;top:2560px;width:1200px;text-align:center;color:var(--white);font-size:42px}
.card{top:2660px;width:312px;height:300px;background:var(--white);padding:24px}
.stars{color:#f5a623;font-size:18px;letter-spacing:3px}
.card p{font-size:14px;line-height:21px;color:var(--muted);margin:12px 0 22px}
.card .rule{border-top:1px solid var(--line);padding-top:14px}
.card h4{font-size:20px}
.card small{font-size:14px;color:var(--muted)}
.arrow{top:2790px}

/* gallery */
.gallery-title{left:0;top:3160px;width:1200px;text-align:center;font-size:42px}
.t1{left:112px;top:3240px;width:484px;height:530px;background:linear-gradient(160deg,#8a6d58,#3c3a3f 60%,#2b6a8c)}
.t2{left:608px;top:3240px;width:480px;height:230px;background:radial-gradient(circle at 50% 50%,#e0a15a,#c9d6de 70%)}
.t3{left:608px;top:3482px;width:232px;height:288px;background:radial-gradient(circle at 50% 45%,#efe6d8,#d9a46b 60%,#b9cfd8)}
.t4{left:852px;top:3482px;width:236px;height:288px;background:radial-gradient(circle at 50% 50%,#c98d52,#6d4d3a 70%)}

/* footer */
.footer{left:0;top:3796px;width:1200px;height:384px;background:var(--blue)}
.foot-h{color:var(--white);font-size:20px}
.links{left:112px;top:3920px;color:var(--white);font-size:14px;line-height:22px;list-style:none}
.links li::before{content:"› ";}
.news-input{left:436px;top:3916px;width:334px;height:46px;border:2px solid var(--white);border-radius:26px;color:var(--white);font-size:14px;padding:0 20px;display:flex;align-items:center}
.news-btn{left:530px;top:3976px;width:120px;height:40px}
.contact{left:848px;top:3916px;color:var(--white);font-size:14px;line-height:20px}
.contact li{list-style:none;display:flex;gap:10px;margin-bottom:14px}
.bar{left:0;top:4090px;width:1200px;height:90px;background:var(--blue-dark)}
.socials{left:112px;top:4120px;display:flex;gap:10px}
.socials span{width:30px;height:30px;border-radius:50%;background:var(--white)}
.copy{left:560px;top:4126px;width:530px;text-align:right;color:var(--white);font-size:14px}
</style>
</head>
<body>

<!-- Hero -->
<div class="abs hero" role="img" aria-label="Groomer bathing a dog in a bright blue grooming van"></div>
<div class="abs hero-shade"></div>
<div class="abs brand head-font">Tail Meadow</div>
<nav class="abs nav"><span class="active">HOME</span><span>LOCATIONS</span><span>CAREERS</span><span>ABOUT</span><span>BLOG</span><span>FAQ</span></nav>
<div class="abs btn btn-green call">Call Now +1 555 014 2290</div>
<h1 class="abs hero-title head-font">Doorstep<br>Dog Grooming</h1>
<p class="abs hero-text">Fresh, calm and caring grooming brought right to your home, so your dog stays relaxed from start to finish.</p>
<div class="abs btn btn-green book">Book Online ›</div>

<form class="abs form">
  <h2 class="head-font">Make an Appointment</h2>
  <div class="row"><div class="field">First name</div><div class="field">Last name</div></div>
  <div class="row"><div class="field">Primary phone</div><div class="field">Mobile</div></div>
  <div class="field">Email address</div>
  <div class="field select">Select your state <span>▾</span></div>
  <div class="submit">SUBMIT</div>
</form>

<!-- Why choose us -->
<div class="abs why-photo" role="img" aria-label="Golden retriever sitting"></div>
<h2 class="abs why-title head-font">Why Choose Us</h2>
<div class="abs perks">
  <div class="perk"><svg width="100" height="100" viewBox="0 0 100 100"><circle cx="50" cy="50" r="48" fill="none" stroke="#3db42f" stroke-width="3"/><circle cx="50" cy="50" r="40" fill="#3db42f"/><path d="M50 30c-8 12-12 18-12 24a12 12 0 0024 0c0-6-4-12-12-24z" fill="#fff"/></svg>Warm Filtered<br>Water Bath</div>
  <div class="perk"><svg width="100" height="100" viewBox="0 0 100 100"><circle cx="50" cy="50" r="48" fill="none" stroke="#3db42f" stroke-width="3"/><circle cx="50" cy="50" r="40" fill="#3db42f"/><path d="M34 66c0-20 14-32 34-34-2 20-14 34-34 34zm0 0l16-16" fill="#fff" stroke="#3db42f" stroke-width="2"/></svg>All Natural<br>Products</div>
  <div class="perk"><svg width="100" height="100" viewBox="0 0 100 100"><circle cx="50" cy="50" r="48" fill="none" stroke="#3db42f" stroke-width="3"/><circle cx="50" cy="50" r="40" fill="#3db42f"/><path d="M36 64l20-20" stroke="#fff" stroke-width="6" stroke-linecap="round"/><rect x="52" y="28" width="18" height="18" rx="3" fill="#fff" transform="rotate(45 61 37)"/></svg>Gentle Brush &amp;<br>Blowout</div>
  <div class="perk"><svg width="100" height="100" viewBox="0 0 100 100"><circle cx="50" cy="50" r="48" fill="none" stroke="#3db42f" stroke-width="3"/><circle cx="50" cy="50" r="40" fill="#3db42f"/><g fill="#fff"><ellipse cx="50" cy="58" rx="10" ry="8"/><circle cx="38" cy="45" r="4"/><circle cx="46" cy="38" r="4"/><circle cx="54" cy="38" r="4"/><circle cx="62" cy="45" r="4"/></g></svg>Trim &amp; File<br>Nails</div>
  <div class="perk"><svg width="100" height="100" viewBox="0 0 100 100"><circle cx="50" cy="50" r="48" fill="none" stroke="#3db42f" stroke-width="3"/><circle cx="50" cy="50" r="40" fill="#3db42f"/><path d="M38 36c6-4 18-4 24 0 4 6 0 14-2 20l-3 12-4-10h-6l-4 10-3-12c-2-6-6-14-2-20z" fill="#fff"/></svg>Clean Teeth<br>&amp; Ears</div>
  <div class="perk"><svg width="100" height="100" viewBox="0 0 100 100"><circle cx="50" cy="50" r="48" fill="none" stroke="#3db42f" stroke-width="3"/><circle cx="50" cy="50" r="40" fill="#3db42f"/><g stroke="#fff" stroke-width="4" fill="none"><circle cx="38" cy="62" r="6"/><circle cx="62" cy="62" r="6"/><path d="M42 57l20-26M58 57L38 31"/></g></svg>Breed Specific<br>Pro Groom</div>
</div>

<!-- Video -->
<div class="abs video" role="img" aria-label="Groomer brushing a spaniel's ears"></div>
<svg class="abs play" width="88" height="88" viewBox="0 0 88 88"><circle cx="44" cy="44" r="42" fill="#fff"/><path d="M36 30l22 14-22 14z" fill="#3db42f"/></svg>

<!-- About -->
<h2 class="abs about-title head-font">About <span>Tail Meadow</span></h2>
<div class="abs about-text">
  <p>Our mobile salon parks right outside your door. Every groom starts with a calm hello, a warm filtered bath and gentle products chosen for your dog's coat and skin, followed by a careful brush, dry and trim by a trained stylist who knows the breed.</p>
  <p>We keep sessions one dog at a time, so there are no crates, no waiting rooms and no stress. Owners get a short update after each visit with notes on coat health, nails and ears, plus tips to keep that fresh look at home until the next booking.</p>
</div>
<div class="abs btn btn-green learn">Learn More ›</div>
<div class="abs about-photo" role="img" aria-label="Smiling owner holding a small dog"></div>

<!-- Testimonials -->
<div class="abs reviews" role="img" aria-label="Green band with a faint grooming scene"></div>
<h2 class="abs reviews-title head-font">Here's What Pet Parents Have To Say</h2>
<svg class="abs arrow" style="left:40px" width="24" height="40" viewBox="0 0 24 40"><path d="M20 4L4 20l16 16" stroke="#222" stroke-width="4" fill="none"/></svg>
<svg class="abs arrow" style="left:1136px" width="24" height="40" viewBox="0 0 24 40"><path d="M4 4l16 16L4 36" stroke="#222" stroke-width="4" fill="none"/></svg>
<div class="abs card" style="left:108px"><div class="stars">★★★★★</div><p>The van pulled up right on time and our terrier came back soft, calm and smelling lovely. Booking was quick and the stylist was kind and patient.</p><div class="rule"><h4>Mara Quinn</h4><small>Company name</small></div></div>
<div class="abs card" style="left:444px"><div class="stars">★★★★★</div><p>Our older lab hates car rides, so grooming at home has been a relief. The nail trim was gentle and the coat looks great for weeks after.</p><div class="rule"><h4>Mara Quinn</h4><small>Company name</small></div></div>
<div class="abs card" style="left:780px"><div class="stars">★★★★★</div><p>Friendly team, clear prices and a happy pup every time. We love the little notes after each visit and the breed cut was spot on.</p><div class="rule"><h4>Mara Quinn</h4><small>Company name</small></div></div>

<!-- Gallery -->
<h2 class="abs gallery-title head-font">Meadow Moments</h2>
<div class="abs t1" role="img" aria-label="Groomer trimming a small terrier"></div>
<div class="abs t2" role="img" aria-label="Fluffy pomeranian after grooming"></div>
<div class="abs t3" role="img" aria-label="Small dog being brushed"></div>
<div class="abs t4" role="img" aria-label="Puppy on a grooming table"></div>

<!-- Footer -->
<footer>
  <div class="abs footer"></div>
  <h3 class="abs foot-h head-font" style="left:112px;top:3866px">Let's Connect</h3>
  <ul class="abs links"><li>Home</li><li>About us</li><li>Services</li><li>Locations</li><li>Careers</li><li>Terms of Service</li></ul>
  <h3 class="abs foot-h head-font" style="left:436px;top:3866px">Sign Up For Our Newsletter</h3>
  <div class="abs news-input">Email address</div>
  <div class="abs btn btn-green news-btn">Submit</div>
  <h3 class="abs foot-h head-font" style="left:848px;top:3866px">Contact Us</h3>
  <ul class="abs contact">
    <li><svg width="14" height="18" viewBox="0 0 14 18"><path d="M7 0a7 7 0 017 7c0 5-7 11-7 11S0 12 0 7a7 7 0 017-7z" fill="#fff"/><circle cx="7" cy="7" r="2.5" fill="#1a7fd6"/></svg><span>Serving homes across the valley,<br>seven days a week</span></li>
    <li><svg width="16" height="16" viewBox="0 0 16 16"><path d="M3 1l3 3-2 2a9 9 0 006 6l2-2 3 3-2 2C7 15 1 9 1 3z" fill="#fff"/></svg><span>+1 555 014 2290</span></li>
    <li><svg width="16" height="12" viewBox="0 0 16 12"><rect width="16" height="12" rx="1" fill="#fff"/><path d="M1 1l7 6 7-6" stroke="#1a7fd6" fill="none"/></svg><span>hello@tailmeadow.example</span></li>
  </ul>
  <div class="abs bar"></div>
  <div class="abs socials"><span></span><span></span><span></span></div>
  <div class="abs copy">© 2021 Tail Meadow | All Rights Reserved | Terms and Conditions</div>
</footer>

</body>
</html>
```